Torvane PT Business Card

I need the card to be bright/bold colours to stand out amongst others.
It needs to have my company logo.
I was not interested in pictures etc just a layout that attracts attention.

I have attached my old design which is very plain. I also needed change the contact details. And my description changed to Personal Trainer
Phone 0427391058
Facebook Torvane PT
No email address please, no street address.
And only Torvane PT (Please remove anything to do with Torvane Supplements)

```html
<!DOCTYPE html>
<html lang="en">
<head>
<meta charset="utf-8">
<title>Torvane PT Business Card</title>
<link rel="stylesheet" href="https://fonts.googleapis.com/css2?family=Open+Sans:wght@400;600;800&display=swap">
<style>
  :root {
    --stage: #262626;
    --card-white: #ffffff;
    --brand-blue: #0b87c9;
    --brand-yellow: #ffdd00;
    --text-grey: #333333;
  }
  html, body {
    margin: 0;
    padding: 0;
    width: 1200px;
    height: 987px;
    overflow: hidden;
    background: var(--stage);
    font-family: "Open Sans", sans-serif;
  }
  .canvas {
    position: relative;
    width: 1200px;
    height: 987px;
  }
  .card {
    position: absolute;
    left: 293px;
    width: 615px;
    height: 351px;
    overflow: hidden;
  }
  .card-front { top: 130px; background: var(--card-white); }
  .card-back { top: 505px; background: var(--brand-blue); }

  .brand-name {
    position: absolute;
    margin: 0;
    font-weight: 800;
    letter-spacing: 1px;
    line-height: 1;
  }
  .card-front .brand-name {
    right: 32px;
    top: 46px;
    font-size: 42px;
    color: var(--brand-blue);
  }
  .card-back .brand-name {
    left: 0;
    right: 0;
    top: 150px;
    text-align: center;
    font-size: 52px;
    color: var(--card-white);
  }

  .holder {
    position: absolute;
    left: 30px;
    top: 196px;
  }
  .holder-name {
    margin: 0;
    font-size: 23px;
    font-weight: 600;
    color: var(--brand-blue);
    line-height: 1.1;
  }
  .holder-role {
    margin: 2px 0 0;
    font-size: 17px;
    color: var(--brand-yellow);
    line-height: 1.1;
  }
  .contact-list {
    list-style: none;
    margin: 12px 0 0;
    padding: 0;
    font-size: 16px;
    color: var(--text-grey);
  }
  .contact-list li {
    display: flex;
    align-items: center;
    gap: 8px;
    height: 24px;
  }
  .contact-icon { width: 15px; height: 15px; flex: none; }
  .social-square {
    width: 14px;
    height: 14px;
    background: var(--brand-blue);
    flex: none;
  }

  .footer-band { position: absolute; left: 0; bottom: 0; }
</style>
</head>
<body>
<main class="canvas">
  <section class="card card-front" aria-label="Card front">
    <p class="brand-name">TORVANE PT</p>

    <div class="holder">
      <h1 class="holder-name">DANA HOLLIS</h1>
      <p class="holder-role">Personal Trainer</p>
      <ul class="contact-list">
        <li>
          <svg class="contact-icon" viewBox="0 0 24 24" aria-hidden="true">
            <path fill="#0b87c9" d="M6.6 10.8a15.1 15.1 0 0 0 6.6 6.6l2.2-2.2c.3-.3.7-.4 1-.2 1.1.4 2.3.6 3.6.6.6 0 1 .4 1 1V20c0 .6-.4 1-1 1A17 17 0 0 1 3 4c0-.6.4-1 1-1h3.5c.6 0 1 .4 1 1 0 1.3.2 2.5.6 3.6.1.3 0 .7-.2 1z"/>
          </svg>
          <span>0427391058</span>
        </li>
        <li>
          <span class="social-square" aria-hidden="true"></span>
          <span>Torvane PT</span>
        </li>
      </ul>
    </div>

    <svg class="footer-band" width="615" height="40" viewBox="0 0 615 40" aria-hidden="true">
      <rect x="0" y="28" width="360" height="12" fill="#0b87c9"/>
      <path d="M346 40 C350 18 362 6 392 0 L615 0 L615 40 Z" fill="#ffdd00"/>
    </svg>
  </section>

  <section class="card card-back" aria-label="Card back">
    <p class="brand-name">TORVANE PT</p>
  </section>
</main>
</body>
</html>
```